Wedding snapchat geofilter.

I need some graphic design. Design a snapchat geofilter for a wedding occasion , Karim ( groom ) & Lina (bride ) it could be the initlas. You may add the wedding date ( May 12th, 2016 ).

Logo please

```html
<!DOCTYPE html>
<html lang="en">
<head>
<meta charset="utf-8">
<title>Karim &amp; Lina Wedding Geofilter</title>
<link rel="stylesheet" href="https://fonts.googleapis.com/css2?family=Pinyon+Script&family=Cormorant+Garamond:ital,wght@1,500&display=swap">
<style>
  :root {
    --paper: #ffffff;
    --silver-ink: #5f6062;
    --silver-light: #d9d9db;
    --silver-mid: #c4c4c8;
    --gold-deep: #d1a431;
    --gold-soft: #efe2b4;
    --gold-ring: #e2a324;
  }
  html, body {
    margin: 0;
    padding: 0;
    width: 675px;
    height: 1200px;
    overflow: hidden;
    background: var(--paper);
  }
  .geofilter {
    position: relative;
    width: 675px;
    height: 1200px;
    background: var(--paper);
  }
  .script {
    position: absolute;
    margin: 0;
    font-family: "Pinyon Script", cursive;
    font-weight: 400;
    color: var(--silver-ink);
    text-shadow: 1px 1px 0 var(--silver-light), -1px -1px 0 #ffffff;
    line-height: 1;
    white-space: nowrap;
  }
  .headline {
    left: 0;
    width: 675px;
    top: 8px;
    text-align: center;
    font-size: 84px;
  }
  .header-flourish {
    position: absolute;
    left: 58px;
    top: 84px;
    width: 562px;
    height: 96px;
  }
  .wreath {
    position: absolute;
    left: 18px;
    top: 716px;
    width: 644px;
    height: 448px;
  }
  .name-flourish {
    position: absolute;
    left: 398px;
    top: 772px;
    width: 162px;
    height: 158px;
    border-radius: 50%;
    background: radial-gradient(circle, #ececee 0%, #f7f7f8 60%, rgba(255,255,255,0) 72%);
  }
  .rings {
    position: absolute;
    left: 106px;
    top: 900px;
    width: 160px;
    height: 100px;
    border-radius: 50%;
    background: linear-gradient(135deg, #f6cf5f 0%, var(--gold-ring) 55%, #b97d12 100%);
  }
  .groom {
    left: 146px;
    top: 770px;
    font-size: 118px;
  }
  .ampersand {
    left: 286px;
    top: 880px;
    font-size: 112px;
  }
  .bride {
    left: 292px;
    top: 940px;
    font-size: 130px;
  }
  .wedding-date {
    position: absolute;
    right: 48px;
    top: 1154px;
    margin: 0;
    font-family: "Cormorant Garamond", serif;
    font-style: italic;
    font-weight: 500;
    font-size: 42px;
    letter-spacing: 6px;
    color: var(--silver-ink);
    text-shadow: 1px 1px 0 var(--silver-light);
    line-height: 1;
  }
</style>
</head>
<body>
  <main class="geofilter">
    <h1 class="script headline">Celebrating</h1>

    <div class="header-flourish" role="img" aria-label="Silver leafy vine flourish beneath the headline">
      <svg width="562" height="96" viewBox="0 0 562 96">
        <defs>
          <linearGradient id="vineTone" x1="0" y1="0" x2="1" y2="0">
            <stop offset="0" stop-color="#ffffff" stop-opacity="0"/>
            <stop offset="0.3" stop-color="#e4e4e7"/>
            <stop offset="0.7" stop-color="#e4e4e7"/>
            <stop offset="1" stop-color="#ffffff" stop-opacity="0"/>
          </linearGradient>
        </defs>
        <rect x="0" y="20" width="562" height="56" rx="28" fill="url(#vineTone)"/>
      </svg>
    </div>

    <div class="wreath" role="img" aria-label="Gold laurel wreath framing the couple's names">
      <svg width="644" height="448" viewBox="0 0 644 448">
        <defs>
          <linearGradient id="laurelTone" x1="0" y1="0" x2="0" y2="1">
            <stop offset="0" stop-color="var(--gold-soft)"/>
            <stop offset="0.55" stop-color="var(--gold-deep)"/>
            <stop offset="1" stop-color="var(--gold-soft)"/>
          </linearGradient>
        </defs>
        <path d="M290 4 C120 30 0 150 14 270 C26 370 150 430 290 440 C180 410 66 350 58 262 C48 160 150 60 290 4 Z" fill="url(#laurelTone)"/>
        <path d="M354 4 C524 30 644 150 630 270 C618 370 494 430 354 440 C464 410 578 350 586 262 C596 160 494 60 354 4 Z" fill="url(#laurelTone)"/>
      </svg>
    </div>

    <div class="name-flourish" role="img" aria-label="Silver swirl flourish beside the names"></div>

    <div class="rings" role="img" aria-label="Two interlocked gold wedding rings"></div>

    <p class="script groom">Karim</p>
    <p class="script ampersand">&amp;</p>
    <p class="script bride">Lina</p>

    <p class="wedding-date">5.12.16</p>
  </main>
</body>
</html>
```